Cedar Hollow Nectar Co.

Using the logo created by your designer I need to have a label made for retail sales of my product (Local Raw Honey) local and raw are the key phrases that would need to stand out to the consumer on the grocery shelves or farmers markets and that this is a 100% pure product. The label will also need to include Net weight in pounds and kg with space for me to write in the numerals as I have multiple size jars (I've included my home made label for reference on the Net weight requirements for my state) and I will need my business name and address "Cedar Holow Nectar Co. 4817 Wexley Rd SW South Danfield Mi. 49372" at the bottom of the of the label.

```html
<!DOCTYPE html>
<html lang="en">
<head>
<meta charset="utf-8">
<title>Cedar Hollow Nectar Co. – Honey Jar Label</title>
<link href="https://fonts.googleapis.com/css2?family=Caprasimo&display=swap" rel="stylesheet">
<style>
  :root {
    --ink: #58595b;
    --amber: #a06a2c;
    --gold: #e8a321;
    --wax: #dcd9cc;
    --paper: #ffffff;
    --rule: #4a4a4a;
  }
  * { margin: 0; padding: 0; box-sizing: border-box; }
  html, body { width: 1200px; height: 675px; overflow: hidden; background: var(--paper); }
  body { position: relative; font-family: "Caprasimo", Georgia, serif; color: var(--ink); }

  .label {
    position: absolute; top: 121px; width: 445px; height: 445px;
    border: 1px solid var(--rule); background: var(--paper);
  }
  .label--front { left: 137px; }
  .label--back { left: 633px; }

  .label__band {
    position: absolute; left: 0; right: 0; bottom: 0; height: 45px;
    background: var(--amber); color: #fff;
    display: flex; align-items: center; justify-content: center;
    font-size: 15px; letter-spacing: 0.2px;
  }
  .label__band--web { font-size: 12.5px; }

  .side-caption {
    position: absolute; top: 596px; width: 445px; text-align: center;
    font-size: 27px; letter-spacing: 0.5px; color: var(--ink);
  }
  .side-caption--front { left: 137px; }
  .side-caption--back { left: 633px; }

  /* brand mark stand-in */
  .brand { position: absolute; display: flex; align-items: center; gap: 8px; color: var(--amber); }
  .brand__dot { border-radius: 50%; background: var(--wax); flex: none; }
  .brand__name { line-height: 1.05; }
  .brand--small { left: 30px; top: 30px; }
  .brand--small .brand__dot { width: 44px; height: 44px; }
  .brand--small .brand__name { font-size: 14px; }
  .brand--large { left: 0; right: 0; top: 178px; flex-direction: column; gap: 10px; }
  .brand--large .brand__dot { width: 90px; height: 90px; }
  .brand--large .brand__name { font-size: 22px; text-align: center; }

  /* purity badge */
  .purity { position: absolute; left: 314px; top: 34px; width: 86px; text-align: center; }
  .purity__figure { font-size: 25px; line-height: 1; color: var(--ink); }
  .purity__tag {
    margin-top: 3px; background: var(--gold); color: #fff;
    border-radius: 12px 0 0 0; padding: 3px 0 4px; line-height: 1;
  }
  .purity__word { display: block; font-size: 20px; }
  .purity__sub { display: block; font-size: 10px; margin-top: 2px; letter-spacing: 0.4px; }

  /* product title stack */
  .title { position: absolute; left: 0; right: 0; top: 122px; text-align: center; line-height: 1; }
  .title__maker { font-size: 27px; }
  .title__local { font-size: 64px; margin-top: 4px; letter-spacing: -1px; }
  .title__raw { font-size: 84px; margin-top: 0; letter-spacing: -1px; }
  .title__variety { font-size: 31px; margin-top: 4px; }
  .title__honey { font-size: 56px; color: var(--amber); margin-top: 2px; letter-spacing: 0.5px; }
  .title__tagline { font-size: 14px; margin-top: 14px; line-height: 1.05; }

  /* back copy */
  .notice { position: absolute; left: 0; right: 0; text-align: center; font-size: 13px; line-height: 1.2; }
  .notice--disclaimer { top: 46px; }
  .notice--process { top: 123px; }
  .notice--address { top: 332px; }
</style>
</head>
<body>

<section class="label label--front" aria-label="Front label">
  <div class="brand brand--small">
    <span class="brand__dot"></span>
    <span class="brand__name">CEDAR HOLLOW<br>NECTAR CO.</span>
  </div>

  <div class="purity">
    <div class="purity__figure">100%</div>
    <div class="purity__tag">
      <span class="purity__word">PURE</span>
      <span class="purity__sub">PRODUCT</span>
    </div>
  </div>

  <div class="title">
    <div class="title__maker">MAE’S HONEY</div>
    <div class="title__local">LOCAL</div>
    <div class="title__raw">RAW</div>
    <div class="title__variety">WILDFLOWER</div>
    <div class="title__honey">HONEY</div>
    <div class="title__tagline">BROUGHT TO YOU BY LOCAL<br>MICHIGAN BEE’S</div>
  </div>

  <div class="label__band">NET WT. 16 OZ (.45 kg)</div>
</section>

<section class="label label--back" aria-label="Back label">
  <p class="notice notice--disclaimer">DISCLAIMER: PROCESSED IN A FACILITY NOT<br>INSPECTED BY THE DEPARTMENT OF<br>AGRICULTURE &amp; RURAL DEVELOPMENT</p>
  <p class="notice notice--process">MINIMALLLY FILTERED<br>ALL PACKAGING PRODUCED IN THE USA</p>

  <div class="brand brand--large">
    <span class="brand__dot"></span>
    <span class="brand__name">Cedar Hollow Nectar Co.</span>
  </div>

  <p class="notice notice--address">CEDAR HOLLOW BEE CO<br>4817 WEXLEY RD SW SOUTH DANFIELD MI 49372</p>

  <div class="label__band label__band--web">WWW.CEDARHOLLOWNECTAR.COM</div>
</section>

<div class="side-caption side-caption--front">FRONT</div>
<div class="side-caption side-caption--back">BACK</div>

</body>
</html>
```